Belford & Company

We are a boutique commercial real estate firm. For our Business card design - sleek, modern, yet high-end/classy. Please see our website: belfordandcompany.example for details.

We currently need 2 business card names and the ability to add/change the business card information -
Name, Title, Address, Office #, Mobile #, Fax, Email and company website.

Industry/Entity Type

Real Estate

Contact Information for Business Card

Business card design - sleek, modern, yet high-end/classy. Please see our website: belfordandcompany.example for details.

Also, we'd like to have our slogan "Dedication Shapes The Outcome." somewhere in there. We'd like to make some part of it raised or a different texture if possible.
Color #'s:
blue 19 36 128
light gray 222 222 221
dark gray 107 120 128

Also, we'd like to have our slogan "Dedication Shapes The Outcome." somewhere in there. We'd like to make some part of it raised or a different texture if possible - grey on one side and blue on the other - rounded edges preferred. Maybe either metal/silver/grey raised logo on the back. Thank you!!

Requirements
Must have
• Sleek, modern, clean and classy design

```html
<!DOCTYPE html>
<html lang="en">
<head>
<meta charset="utf-8">
<title>Belford &amp; Company — Business Card</title>
<link rel="stylesheet" href="https://fonts.googleapis.com/css2?family=Cinzel:wght@400;600&family=Arimo:wght@400&display=swap">
<style>
  :root {
    --brand-blue: rgb(19, 36, 128);
    --brand-blue-light: #2a4fc0;
    --light-gray: rgb(222, 222, 221);
    --dark-gray: rgb(107, 120, 128);
    --ink: #111111;
    --paper: #ffffff;
    --backdrop: #e7e5e1;
  }
  * { margin: 0; padding: 0; box-sizing: border-box; }
  html, body {
    width: 1200px;
    height: 1200px;
    overflow: hidden;
    background: var(--backdrop);
  }
  .canvas {
    position: relative;
    width: 1200px;
    height: 1200px;
  }
  .card {
    position: absolute;
    left: 240px;
    width: 720px;
    height: 410px;
    border-radius: 32px;
    box-shadow: 0 14px 30px rgba(0, 0, 0, 0.22);
    overflow: hidden;
  }

  /* Front: blue side */
  .card--front {
    top: 130px;
    background: linear-gradient(135deg, var(--brand-blue-light) 0%, var(--brand-blue) 55%, #1b3da6 100%);
  }
  .front-logo {
    position: absolute;
    left: 44px;
    top: 58px;
    display: flex;
    align-items: center;
    gap: 14px;
  }
  .logo-square {
    width: 22px;
    height: 22px;
    background: var(--light-gray);
  }
  .logo-name {
    font-family: 'Cinzel', serif;
    font-weight: 600;
    font-size: 38px;
    letter-spacing: 2px;
    line-height: 1;
  }
  .front-logo .logo-name { color: var(--light-gray); }
  .front-rule {
    position: absolute;
    left: 44px;
    top: 112px;
    width: 330px;
    height: 1px;
    background: var(--dark-gray);
    opacity: 0.8;
  }
  .front-tagline {
    position: absolute;
    right: 48px;
    bottom: 42px;
    font-family: 'Arimo', sans-serif;
    font-size: 27px;
    color: var(--light-gray);
    text-shadow: 0 1px 0 rgba(0, 0, 0, 0.35);
  }

  /* Back: white side */
  .card--back {
    top: 640px;
    background: var(--paper);
  }
  .back-logo {
    position: absolute;
    right: 44px;
    top: 44px;
    display: flex;
    align-items: center;
    gap: 12px;
  }
  .back-logo .logo-square { background: var(--dark-gray); width: 18px; height: 18px; }
  .back-logo .logo-name { color: var(--dark-gray); font-size: 30px; }
  .back-rule {
    position: absolute;
    right: 44px;
    top: 92px;
    width: 260px;
    height: 1px;
    background: var(--dark-gray);
  }
  .holder-name {
    position: absolute;
    left: 66px;
    top: 130px;
    font-family: 'Cinzel', serif;
    font-weight: 400;
    font-size: 38px;
    letter-spacing: 1px;
    color: var(--ink);
  }
  .contact-list {
    position: absolute;
    left: 66px;
    bottom: 46px;
    list-style: none;
    font-family: 'Arimo', sans-serif;
    font-size: 18px;
    line-height: 1.3;
    color: var(--ink);
  }
  .contact-list .email { font-size: 15px; }
  .website {
    position: absolute;
    right: 44px;
    bottom: 52px;
    font-family: 'Cinzel', serif;
    font-size: 13px;
    letter-spacing: 2px;
    color: var(--ink);
  }
</style>
</head>
<body>
<main class="canvas">
  <section class="card card--front" aria-label="Business card front">
    <div class="front-logo">
      <span class="logo-square" aria-hidden="true"></span>
      <span class="logo-name">Belford &amp; Company</span>
    </div>
    <div class="front-rule" aria-hidden="true"></div>
    <p class="front-tagline">Dedication Shapes The Outcome</p>
  </section>

  <section class="card card--back" aria-label="Business card back">
    <div class="back-logo">
      <span class="logo-square" aria-hidden="true"></span>
      <span class="logo-name">Belford &amp; Company</span>
    </div>
    <div class="back-rule" aria-hidden="true"></div>
    <h1 class="holder-name">Marcus Hale</h1>
    <ul class="contact-list">
      <li class="phone">(00) 00000-0000</li>
      <li class="phone">(00) 00000-0000</li>
      <li class="email">contact@belfordcompany.example</li>
    </ul>
    <p class="website">www . belfordandcompany . example</p>
  </section>
</main>
</body>
</html>
```